Informative Infografiken für Matratzenhersteller
Zielgruppe
Produzent von Matratzen, Zielgruppe ist daher jeder der eine neue Matratze benötigt
Aufgabenstellung
Die Infografik soll auf einer Webseite implementiert werden. Es wäre daher schön, wenn die CI Farben #63b32f und #343A40 eingebunden werden könnten.
Die Infografik soll schnell Informationen zu folgende Themen ersichtlich machen: Härtegrad, Raumgewicht, Matratze für verschiedene Schlaftypen

```html
<!DOCTYPE html>
<html lang="de">
<head>
<meta charset="utf-8">
<title>Matratzen-Infografik</title>
<link href="https://fonts.googleapis.com/css2?family=PT+Sans+Narrow&family=PT+Sans&display=swap" rel="stylesheet">
<style>
  :root {
    --ci-green: #63b32f;
    --green-1: #55ad34;
    --green-2: #7cb85a;
    --green-3: #94bf78;
    --green-4: #a3c58e;
    --ci-dark: #343A40;
    --panel: #cfcfcc;
    --muted: #6f6f6f;
    --paper: #ffffff;
  }
  html, body { margin: 0; padding: 0; }
  body {
    width: 1200px; height: 894px; overflow: hidden;
    background: var(--paper); position: relative;
    font-family: "PT Sans Narrow", sans-serif; color: var(--ci-dark);
  }
  .panel { position: absolute; top: 39px; width: 337px; height: 822px; background: var(--panel); }
  .panel--hardness { left: 66px; }
  .panel--density { left: 444px; }
  .panel--sleeper { left: 817px; }
  .abs { position: absolute; }
  .illustration {
    position: absolute;
    background: linear-gradient(180deg, #3c4248 0%, var(--ci-dark) 55%, var(--green-1) 100%);
    border-radius: 40px 40px 14px 14px; opacity: .9;
  }
  .heading { position: absolute; font-size: 30px; line-height: 1; margin: 0; font-weight: 400; }
  .copy { position: absolute; font-size: 19px; line-height: 21.5px; letter-spacing: -0.6px; margin: 0; }
  .copy--muted { color: var(--muted); line-height: 23.7px; }
  .spec-list { position: absolute; font-family: "PT Sans", sans-serif; font-size: 17px; line-height: 21.3px; margin: 0; }
  .bar-label { position: absolute; color: #fff; font-size: 27px; line-height: 1; }
  .tag-label { position: absolute; color: #fff; font-size: 24px; line-height: 1; }
  .grade { position: absolute; color: #fff; font-size: 22px; width: 40px; text-align: center; line-height: 1; }
  .grade-text { position: absolute; font-family: "PT Sans", sans-serif; font-size: 16.5px; line-height: 18px; }
  .pill {
    position: absolute; width: 147px; height: 37px; border-radius: 19px;
    color: #fff; font-size: 22px; line-height: 37px; text-align: center;
  }
  .sleeper-list { position: absolute; font-family: "PT Sans", sans-serif; font-size: 17.5px; line-height: 21.5px; margin: 0; }
  .sleeper-list .detail { padding-left: 14px; display: block; }
  .sleeper-list .item { margin-bottom: 10px; }
</style>
</head>
<body>

<!-- Härtegrad -->
<section class="panel panel--hardness"></section>
<div class="illustration" role="img" aria-label="Matratze mit Gewicht (Kettlebell) darauf, Federkern darunter" style="left:103px;top:68px;width:273px;height:229px;"></div>
<svg class="abs" style="left:0;top:0" width="1200" height="894" aria-hidden="true">
  <polygon points="107,395 139,371 171,395 171,537 107,537" fill="var(--green-4)"/>
  <polygon points="171,373 203,350 235,373 235,537 171,537" fill="var(--green-3)"/>
  <polygon points="235,358 267,335 298,358 298,537 235,537" fill="var(--green-2)"/>
  <polygon points="298,338 330,312 362,338 362,537 298,537" fill="var(--green-1)"/>
</svg>
<span class="bar-label" style="left:122px;top:401px;">H2</span>
<span class="bar-label" style="left:189px;top:378px;">H3</span>
<span class="bar-label" style="left:253px;top:364px;">H4</span>
<span class="bar-label" style="left:316px;top:343px;">H5</span>
<h2 class="heading" style="left:106px;top:552px;">Härtegrad</h2>
<p class="copy" style="left:106px;top:594px;">Härtegrad nach Body Mass Index<br>(BMI) bestimmen. Weil neben dem<br>Körpergewicht auch die Körperlänge<br>eine Rolle spielt, können Sie den rich-<br>tigen Härtegrad auch nach BMI aus-<br>wählen.</p>
<p class="copy" style="left:106px;top:743px;">H3 = Gewicht bis 100kg = BMI bis 30<br>H4 = Gewicht bis 130kg = BMI bis 35<br>H5 = Gewicht bis 140kg = BMI bis 40</p>

<!-- Raumgewicht -->
<section class="panel panel--density"></section>
<div class="illustration" role="img" aria-label="Zwei Matratzen auf einer Wippe im Vergleich" style="left:470px;top:76px;width:292px;height:146px;"></div>
<svg class="abs" style="left:0;top:0" width="1200" height="894" aria-hidden="true">
  <g class="cube">
    <polygon points="469,310 505,294 538,310 500,327" fill="#b6d0a4"/>
    <polygon points="469,310 500,327 500,368 469,352" fill="#a9c896"/>
    <polygon points="500,327 538,310 538,352 500,368" fill="#98b788"/>
  </g>
  <g class="cube">
    <polygon points="469,371 505,355 538,371 500,388" fill="#a3c58e"/>
    <polygon points="469,371 500,388 500,418 469,402" fill="#9cc185"/>
    <polygon points="500,388 538,371 538,402 500,418" fill="#85a773"/>
  </g>
  <g class="cube">
    <polygon points="469,419 505,403 538,419 500,436" fill="#8fbf6c"/>
    <polygon points="469,419 500,436 500,466 469,450" fill="#8fbb73"/>
    <polygon points="500,436 538,419 538,450 500,466" fill="#6e9a56"/>
  </g>
  <g class="cube">
    <polygon points="469,468 505,452 538,468 500,485" fill="var(--green-1)"/>
    <polygon points="469,468 500,485 500,514 469,498" fill="#88c05f"/>
    <polygon points="500,485 538,468 538,498 500,514" fill="#3f8a2e"/>
  </g>
  <polygon points="538,313 612,313 627,333 612,354 538,354" fill="var(--green-4)"/>
  <polygon points="538,362 612,362 627,382 612,402 538,402" fill="var(--green-3)"/>
  <polygon points="538,411 612,411 627,430 612,450 538,450" fill="var(--green-2)"/>
  <polygon points="538,459 612,459 627,479 612,498 538,498" fill="var(--green-1)"/>
  <circle cx="660" cy="334" r="20" fill="var(--green-4)"/>
  <circle cx="660" cy="384" r="20" fill="var(--green-3)"/>
  <circle cx="660" cy="432" r="20" fill="var(--green-2)"/>
  <circle cx="660" cy="480" r="20" fill="var(--green-1)"/>
</svg>
<span class="tag-label" style="left:545px;top:323px;">20 - 25</span>
<span class="tag-label" style="left:545px;top:372px;">40</span>
<span class="tag-label" style="left:545px;top:420px;">50 - 60</span>
<span class="tag-label" style="left:548px;top:468px;">75</span>
<span class="grade" style="left:640px;top:323px;">4</span>
<span class="grade" style="left:640px;top:373px;">3</span>
<span class="grade" style="left:640px;top:421px;">2</span>
<span class="grade" style="left:640px;top:469px;">1</span>
<span class="grade-text" style="left:693px;top:315px;">Niedriger<br>Standard</span>
<span class="grade-text" style="left:693px;top:365px;">Gute<br>Qualität</span>
<span class="grade-text" style="left:693px;top:414px;">Sehr hohe<br>Qualität</span>
<span class="grade-text" style="left:693px;top:463px;">Exzellente<br>Qualität</span>
<h2 class="heading" style="left:479px;top:552px;">Raumgewicht</h2>
<p class="copy copy--muted" style="left:479px;top:593px;">Das Raumgewicht gilt als Kennzahl für<br>die Haltbarkeit einer Matratze und gibt<br>an, wie viel Kilogramm Rohmasse in<br>einem Kubikmeter Schaumstoff auf-<br>geschäumt wurden. Je höher, desto<br>schwerer der Schaumstoff und umso<br>höher Langlebigkeit der Matratze.</p>
<p class="spec-list" style="left:481px;top:766px;">4 = Haltbarkeit: etwa 1-2 Jahre<br>3 = Haltbarkeit: etwa 6-8 Jahre<br>2 = Haltbarkeit: etwa 10 Jahre<br>1 = Haltbarkeit: über 10 Jahre</p>

<!-- Schlaftyp -->
<section class="panel panel--sleeper"></section>
<div class="illustration" role="img" aria-label="Schlafende Figur auf einer Matratze mit Federkern" style="left:851px;top:81px;width:276px;height:168px;"></div>
<svg class="abs" style="left:0;top:0" width="1200" height="894" aria-hidden="true">
  <path d="M851,321 A98,95 0 0 1 851,510" fill="none" stroke="var(--green-1)" stroke-width="4"/>
</svg>
<div class="pill" style="left:934px;top:317px;background:var(--green-1);">Bauch</div>
<div class="pill" style="left:965px;top:369px;background:var(--green-2);">Fötus</div>
<div class="pill" style="left:964px;top:423px;background:var(--green-3);">Rücken</div>
<div class="pill" style="left:944px;top:475px;background:var(--green-4);">Seite</div>
<h2 class="heading" style="left:851px;top:552px;">Schlaftyp</h2>
<div class="sleeper-list" style="left:851px;top:594px;">
  <div class="item">1 Der Bauchschläfer<span class="detail">Mit dem Gesicht nach unten</span></div>
  <div class="item">2 Der Fötus-Schläfer<span class="detail">Auf der Seite eingerollt</span></div>
  <div class="item">3 Der Rückenschläfer<span class="detail">Auf dem Rücken,</span><span class="detail">Arme seitlich anliegend</span></div>
  <div class="item">4 Der Seitenschläfer<span class="detail">Auf der Seite eingerollt</span></div>
</div>

</body>
</html>
```